Top Boss Fables - stories about clueless leaders - Book Cover

Need a book cover design which fits the attached template, using materials provided. The book is a collection of short stories with the theme of lampooning clueless Dear Leaders of all kinds. Some stories apply to American politicians, Generals from the Great War, CEO types, cats, ex-wives, the list is endless.

To be considered, final source files must be compatible with Adobe Illustrator, and any art used must not require additional licensing costs.

Font styles to use
Serif

Requirements
Must have
• Must convey it is a work of humor, aimed at the topic.
Nice to have
• We like a concept similar to old soviet heroic art, something like the statues to Ordo family in North Korea for example. Another concept is to riff on Dear Leader from Vadim and Ludmila. Or a collage of such people from history. Key will be an infusion of satire or humor, clearly convey it isn't serious.

```html
<!DOCTYPE html>
<html lang="en">
<head>
<meta charset="utf-8">
<title>Top Boss Fables — Book Cover</title>
<link rel="stylesheet" href="https://fonts.googleapis.com/css2?family=Arimo:ital,wght@0,400;0,700;1,400;1,700&display=swap">
<style>
  :root {
    --paper: #e5e2da;
    --red: #d10a0a;
    --title: #f3e9e2;
    --ink: #111111;
    --art-light: #d8cfc8;
    --art-warm: #d9a9a2;
    --figure: #1a1a1a;
  }
  * { margin: 0; padding: 0; box-sizing: border-box; }
  html, body { width: 1200px; height: 840px; overflow: hidden; background: var(--paper); }
  .cover {
    position: relative;
    width: 1200px;
    height: 840px;
    background: var(--paper);
    font-family: "Arimo", Arial, sans-serif;
    overflow: hidden;
  }
  .band {
    position: absolute;
    top: 0;
    height: 840px;
    width: 164px;
    background: var(--red);
  }
  .band--back { left: 201px; }
  .band--front { left: 843px; }
  .band__title {
    padding-top: 10px;
    text-align: center;
    color: var(--title);
    font-weight: 700;
    font-size: 35px;
    line-height: 41px;
    letter-spacing: 0.5px;
    text-transform: uppercase;
  }
  .blurb {
    position: absolute;
    left: 44px;
    top: 168px;
    width: 486px;
    color: var(--ink);
    font-weight: 700;
    font-style: italic;
    font-size: 13.2px;
    line-height: 16.6px;
    z-index: 2;
  }
  .blurb p + p { margin-top: 16.6px; }
  .publisher {
    position: absolute;
    left: 44px;
    top: 724px;
    display: flex;
    flex-direction: column;
    align-items: flex-start;
    gap: 6px;
  }
  .publisher__mark {
    width: 22px;
    height: 22px;
    background: var(--ink);
  }
  .publisher__name {
    font-size: 12px;
    font-weight: 700;
    color: var(--ink);
    letter-spacing: 1px;
    text-transform: uppercase;
  }
  .eye-art {
    position: absolute;
    left: 663px;
    top: 146px;
    width: 503px;
    height: 335px;
    background: linear-gradient(180deg, var(--art-light), var(--art-warm));
  }
  .figure-art {
    position: absolute;
    left: 867px;
    top: 620px;
    width: 81px;
    height: 77px;
    background: var(--figure);
  }
  .contributors {
    position: absolute;
    left: 1010px;
    top: 752px;
    width: 184px;
    color: var(--red);
    font-style: italic;
    font-size: 11px;
    line-height: 13px;
  }
</style>
</head>
<body>
<main class="cover">
  <div class="band band--back">
    <h2 class="band__title">Top<br>Boss<br>Fables</h2>
  </div>
  <div class="band band--front">
    <h1 class="band__title">Top<br>Boss<br>Fables</h1>
  </div>

  <section class="blurb">
    <p>2020 has been a very trying year for humanity. In addition to a barely-checked viral contagion and widespread economic distress, the usual cavalcade of Top Bosses are doing exactly what they do best: oppressing and dividing the rest of us. These stories and poems are meant to humorously talk truth about power and its misuse. From an orange-haired Wendigo to an Asian Dictator, from CEOs to demons to feline overlords — this wide-ranging collection touches on all manner of oblivious villainy.</p>
    <p>As another contentious American Presidential Election comes to a close, many of us could use a humorous respite and the reminder that our problems are not new or different, just oppression's same old song. Take a break with these clever tales and remember that the things we worry about today will pass and new ones will emerge. This collection will take you to the next screen.</p>
    <p>Featuring original stories and poems by Carla Abbot, Dennis Aulet, Evan Arkwright, Peter L. Bain, June Bellamy, Ben Barrowfield, Walter Brook, Jim Carrow, Dov Calder, Dirk Delane, Bud Dalton, Karina Dubrova, Milo Ekwe, Lewis Everly, Robert Milton Fenn, Anna Gorski, N.E. Gaffney, Laura Stroud, Jill Hart, Lindsey Hale, Wes Ingram, Adrian Jessop, John H. Keller, J.J.J. Kirwan, Ray Lam, Kate Mercer, Tess Malloy, Lina Ngo, Peter Nolan, Mark Norbury, Nina M. Pryce, Jim Rudd, Jeff Selden, Marion S. E. Sloane. Guest editor E. E. Kemp joins this illustrious group as well as in-house authors Don M. Keller and Sara M. Keller.</p>
  </section>

  <div class="publisher">
    <span class="publisher__mark"></span>
    <span class="publisher__name">Stray Tom Press</span>
  </div>

  <div class="eye-art" role="img" aria-label="Engraved-style illustration of a single staring eye with a red iris"></div>
  <div class="figure-art" role="img" aria-label="Black silhouette of a small figure tumbling downward"></div>

  <p class="contributors">Collection of short stories and poems by Evan Arkwright, Anna Gorski, Marion S. E. Sloane, Ray Lam, and many more</p>
</main>
</body>
</html>
```